Business Card Design Project

We are an agricultural business based in Brisbane.
We design, manage and operate regional saleyards. Our logo is green/silver in colour and details of our business can be found on our website www.vodemarketyards.com.au

Just wanting a corporate design for some business cards and include name, position, contact details.

Thanks

Industry/Entity Type

Business

```html
<!DOCTYPE html>
<html lang="en">
<head>
<meta charset="utf-8">
<title>Vode Market Yards – Business Card</title>
<link rel="stylesheet" href="https://fonts.googleapis.com/css2?family=Ubuntu:wght@400;500;700&display=swap">
<style>
  :root {
    --backdrop: #ecebe8;
    --card-white: #ffffff;
    --brand-green: #1f9a4b;
    --ink: #1f2a2e;
    --text-on-band: #ffffff;
  }
  * { margin: 0; padding: 0; box-sizing: border-box; }
  html, body {
    width: 1200px; height: 802px; overflow: hidden;
    background: var(--backdrop);
    font-family: "Ubuntu", sans-serif;
  }
  .business-card {
    position: absolute; left: 100px; top: 98px;
    width: 1000px; height: 606px;
    background: var(--card-white);
    box-shadow: 0 6px 24px rgba(0,0,0,0.18);
    overflow: hidden;
  }
  .card-artwork { position: absolute; inset: 0; }
  .brand-lockup {
    position: absolute; left: 50px; top: 188px;
    display: flex; align-items: center; gap: 14px;
  }
  .brand-square { width: 30px; height: 30px; background: var(--brand-green); flex: none; }
  .brand-name {
    font-weight: 700; font-size: 34px; line-height: 1; color: var(--ink);
    letter-spacing: 0.5px; white-space: nowrap;
  }
  .person {
    position: absolute; right: 40px; top: 190px;
    color: var(--text-on-band); text-align: right;
  }
  .person-name { font-size: 46px; font-weight: 400; line-height: 1.1; letter-spacing: 1px; white-space: nowrap; }
  .person-role { font-size: 20px; font-weight: 500; margin-top: 4px; white-space: nowrap; }
  .contact-list {
    position: absolute; left: 44px; top: 440px;
    list-style: none; color: var(--brand-green);
    font-size: 24px;
  }
  .contact-item { display: flex; align-items: center; gap: 14px; height: 42px; white-space: nowrap; }
  .contact-icon { width: 32px; height: 28px; flex: none; }
  .website {
    position: absolute; right: 40px; top: 470px;
    display: flex; align-items: center; gap: 14px;
    color: var(--text-on-band); font-size: 24px; white-space: nowrap;
  }
  .website-icon { width: 34px; height: 34px; flex: none; }
</style>
</head>
<body>
  <div class="business-card">
    <svg class="card-artwork" viewBox="0 0 1000 606" width="1000" height="606" aria-hidden="true">
      <defs>
        <linearGradient id="band-grey" x1="0" y1="0" x2="1" y2="0">
          <stop offset="0" stop-color="#c4c4c4"/>
          <stop offset="0.6" stop-color="#a6a6a6"/>
          <stop offset="1" stop-color="#8e8e8e"/>
        </linearGradient>
        <linearGradient id="panel-grey" x1="0" y1="0" x2="1" y2="0">
          <stop offset="0" stop-color="#f0f0f0"/>
          <stop offset="1" stop-color="#d2d2d2"/>
        </linearGradient>
      </defs>
      <polygon class="band-panel" points="0,310 1000,170 1000,606 0,606" fill="url(#panel-grey)"/>
      <polygon class="band-main" points="560,170 1000,170 1000,300 600,300 470,420 0,420 0,310 430,310" fill="url(#band-grey)"/>
      <polygon class="band-green" points="620,430 1000,430 1000,606 0,606 0,540 520,540" fill="var(--brand-green)"/>
    </svg>

    <div class="brand-lockup">
      <span class="brand-square"></span>
      <span class="brand-name">VODE MARKET YARDS</span>
    </div>

    <div class="person">
      <p class="person-name">Daniel Hartley</p>
      <p class="person-role">Chief Executive Officer</p>
    </div>

    <ul class="contact-list">
      <li class="contact-item">
        <svg class="contact-icon" viewBox="0 0 34 30" aria-hidden="true">
          <rect x="2" y="5" width="30" height="20" fill="var(--brand-green)"/>
          <polyline points="2,5 17,17 32,5" fill="none" stroke="#fff" stroke-width="2"/>
        </svg>
        <span>daniel@vodemarketyards.com.au</span>
      </li>
      <li class="contact-item">
        <svg class="contact-icon" viewBox="0 0 34 30" aria-hidden="true">
          <rect x="10" y="1" width="14" height="28" rx="3" fill="var(--brand-green)"/>
          <rect x="13" y="5" width="8" height="9" fill="#fff"/>
          <circle cx="17" cy="22" r="2" fill="#fff"/>
        </svg>
        <span>0400 713 952</span>
      </li>
    </ul>

    <div class="website">
      <svg class="website-icon" viewBox="0 0 36 36" aria-hidden="true">
        <circle cx="18" cy="18" r="16" fill="#fff"/>
        <g fill="none" stroke="var(--brand-green)" stroke-width="1.8">
          <circle cx="18" cy="18" r="11"/>
          <ellipse cx="18" cy="18" rx="5" ry="11"/>
          <line x1="7" y1="18" x2="29" y2="18"/>
          <line x1="9" y1="12" x2="27" y2="12"/>
          <line x1="9" y1="24" x2="27" y2="24"/>
        </g>
      </svg>
      <span>www.vodemarketyards.com.au</span>
    </div>
  </div>
</body>
</html>
```